Halloway Crest Backers Guild business cards

Create a single-sided business card for the Halloway Crest Backers Guild based on the attached logo.
The additional data fields include Name, Title, Email, Phone, and website.
Please use the following as sample data:
Name: Dean Varrow
Title: Co-Founder / Investor
Email: deanvarrow@mailtern.net
Phone: 555-314-2706
Website: www.hcbackersguild.com

Target Market(s)

Start ups, entrepreneurs, venture capitalists

Industry/Entity Type

Investment

Contact Information for Business Card

Professional business card. Technology company.

Font styles to use
Serif
Sans Serif

Requirements
Must have
• Include the HCBG logo (attached)
• Name
• Title
• Email
• Phone
• Website
Should not have
• Cute, cartoony

```html
<!DOCTYPE html>
<html lang="en">
<head>
<meta charset="utf-8">
<title>Halloway Crest Backers Guild — Business Card</title>
<link href="https://fonts.googleapis.com/css2?family=Open+Sans:wght@400;600&display=swap" rel="stylesheet">
<style>
  :root {
    --backdrop: #e9e7e3;
    --card: #ffffff;
    --green: #1f8a45;
    --charcoal: #3a3a3a;
    --text: #2b2b2b;
    --shadow: rgba(0,0,0,0.18);
  }
  * { box-sizing: border-box; margin: 0; padding: 0; }
  html, body { width: 1200px; height: 892px; overflow: hidden; }
  body {
    background: var(--backdrop);
    font-family: "Open Sans", sans-serif;
    position: relative;
  }
  .card {
    position: absolute;
    width: 600px;
    height: 343px;
    background: var(--card);
    box-shadow: 0 6px 18px var(--shadow);
  }
  .card--back { left: 540px; top: 70px; }
  .card--front { left: 60px; top: 470px; }

  .brand {
    display: flex;
    align-items: center;
    gap: 14px;
    color: var(--green);
    font-weight: 400;
    line-height: 1.05;
  }
  .brand__dot {
    width: 22px; height: 22px;
    border-radius: 50%;
    background: var(--green);
    flex: none;
  }
  .card--back .brand {
    position: absolute;
    left: 90px; top: 120px;
    font-size: 38px;
    width: 440px;
  }
  .card--front .brand {
    position: absolute;
    left: 0; right: 0; top: 42px;
    justify-content: center;
    font-size: 30px;
  }
  .brand__name { max-width: 380px; }

  .person {
    position: absolute;
    right: 330px; top: 190px;
    text-align: right;
  }
  .person__name { font-size: 26px; color: var(--text); font-weight: 400; }
  .person__title { font-size: 17px; color: var(--green); margin-top: 2px; }

  .divider {
    position: absolute;
    left: 290px; top: 180px;
    width: 2px; height: 100px;
    background: var(--green);
  }

  .contact {
    position: absolute;
    left: 312px; top: 196px;
    list-style: none;
    font-size: 16px;
    color: var(--text);
  }
  .contact li { display: flex; align-items: center; gap: 12px; height: 26px; }
  .contact svg { width: 16px; height: 16px; flex: none; fill: var(--green); }
</style>
</head>
<body>
  <section class="card card--back" aria-label="Card back">
    <div class="brand">
      <span class="brand__dot"></span>
      <span class="brand__name">Halloway Crest Backers Guild</span>
    </div>
  </section>

  <section class="card card--front" aria-label="Card front">
    <div class="brand">
      <span class="brand__dot"></span>
      <span class="brand__name">Halloway Crest Backers Guild</span>
    </div>

    <div class="person">
      <p class="person__name">Dean Varrow</p>
      <p class="person__title">Co-Founder / Investor</p>
    </div>

    <div class="divider"></div>

    <ul class="contact">
      <li>
        <svg viewBox="0 0 16 16" aria-hidden="true"><path d="M3 2h3l1 4-2 1a9 9 0 0 0 4 4l1-2 4 1v3a1 1 0 0 1-1 1A13 13 0 0 1 2 3a1 1 0 0 1 1-1z"/></svg>
        555-314-2706
      </li>
      <li>
        <svg viewBox="0 0 16 16" aria-hidden="true"><path d="M1 3h14v10H1z M2 4l6 5 6-5" fill="none" stroke="#1f8a45" stroke-width="1.5"/></svg>
        deanvarrow@mailtern.net
      </li>
      <li>
        <svg viewBox="0 0 16 16" aria-hidden="true"><g fill="none" stroke="#1f8a45" stroke-width="1.3"><circle cx="8" cy="8" r="6.5"/><ellipse cx="8" cy="8" rx="3" ry="6.5"/><path d="M1.5 8h13M2.5 4.5h11M2.5 11.5h11"/></g></svg>
        www.hcbackersguild.com
      </li>
    </ul>
  </section>
</body>
</html>
```